Early Detection and Diagnosis of Autism - Infographic

Our colors are blue, yellow, and green. A brand color pallette will be attached.

Here is all the information we want to have on our infographic:

Title: Why is Early Detection and Diagnosis of Autism So Important?
Reason 1: An early diagnosis can mean a child gains access to important therapies and resources when they can be the most effective. Without the diagnosis, most insurances won’t cover treatments like ABA therapy.
Reason 2: ABA therapy is shown to be most effective on toddlers and young children because their brains are not completely developed and have an increased potential for developing new learning pathways.
Reason 3: Children who receive early intervention have improved outcomes and increased success and independence in the long run.
We know that early detection and diagnosis works…
Stat 1: Research has shown that a diagnosis of autism at age 2 can be reliable, valid and stable.
Stat 2: Studies have shown that parents of children with ASD notice a developmental problem before their child’s first birthday. Concerns about vision and hearing were more often reported in the first year, and differences in social, communication, and fine motor skills were evident from 6 months of age.

Despite all the good that early detection and diagnosis can do, it hasn’t been as successful as it should be…
Stat 3: In 2016, the QMT conducted a report that showed that only 43 percent of children identified with autism had received comprehensive developmental evaluations by age 3.
Stat 4: According to a QMT study from 2016, even though ASD can be diagnosed as early as age 2 years, most children are not diagnosed with ASD until after age 4 years.

How can you make sure a child doesn’t miss out on key years of intervention? KNOW THE SIGNS
• By 6 months, no social smiles or other warm, joyful expressions directed at people
• By 6 months, limited or no eye contact
• By 9 months, no sharing of vocal sounds, smiles or other nonverbal communication
• By 12 months, no babbling
• By 12 months, no use of gestures to communicate (e.g. pointing, reaching, waving etc.)
• By 12 months, no response to name when called
• By 16 months, no words
• By 24 months, no meaningful, two-word phrases
• Any loss of any previously acquired speech, babbling or social skills

You can help increase the success of early detection by having your child evaluated if you see any of these signs.
Want to learn more about early detection?
Go to: bramblewoodkidsclinic.com/early-detection

Target Market(s)

Moms and Dads of Children with Autism

Industry/Entity Type

Health Care

Font styles to use
Sans Serif

Colors
f78f20
cadf82
fbee3d
fece3e
33b8a4

Requirements
Must have
• Great data visualization. Autism themed illustrations like puzzle pieces (a common theme in design work about autism). Need source file in PSD.

```html
<!DOCTYPE html>
<html lang="en">
<head>
<meta charset="utf-8">
<title>Early Detection and Diagnosis Infographic</title>
<link href="https://fonts.googleapis.com/css2?family=Bebas+Neue&family=Amatic+SC:wght@700&family=Roboto+Condensed:ital,wght@0,400;0,700;1,700&display=swap" rel="stylesheet">
<style>
  :root{
    --navy:#1562a4;
    --navy-deep:#1b3f78;
    --sky:#8fc1df;
    --sky-soft:#b9d9ec;
    --mid-blue:#2a91d4;
    --yellow:#e9b81e;
    --green:#8dba3f;
    --green-dark:#3d9a4a;
    --pink:#d9568c;
    --orange:#e98a2b;
    --ribbon:#7f9fd6;
    --white:#ffffff;
    --ink:#1d3f73;
  }
  *{margin:0;padding:0;box-sizing:border-box}
  html,body{width:848px;height:1200px;overflow:hidden;background:var(--white)}
  .canvas{position:relative;width:848px;height:1200px;overflow:hidden;background:var(--white);font-family:"Roboto Condensed",Arial,sans-serif;color:var(--ink)}
  .abs{position:absolute}

  .header{left:0;top:0;width:848px;height:171px;background:var(--navy)}
  .title-top{left:106px;top:22px;font-family:"Bebas Neue",sans-serif;font-size:72px;line-height:1;color:var(--yellow);letter-spacing:1px}
  .title-bottom{left:106px;top:94px;font-family:"Bebas Neue",sans-serif;font-size:78px;line-height:1;color:var(--white);letter-spacing:1px}
  .ribbon{left:523px;top:34px;width:158px;height:42px;background:var(--ribbon);transform:rotate(-3deg);border-radius:3px;display:flex;align-items:center;justify-content:center;font-family:"Bebas Neue",sans-serif;font-size:22px;color:var(--white)}

  .hand-heading{font-family:"Amatic SC",sans-serif;font-weight:700;color:var(--navy);line-height:1.12}
  .why{left:107px;top:178px;font-size:32px}
  .how{left:522px;top:286px;font-size:31px}
  .works{left:86px;top:872px;font-size:36px}

  .head-art{left:34px;top:258px;width:464px;height:600px;border-radius:230px 230px 40px 120px;background:linear-gradient(160deg,var(--sky-soft),var(--sky))}
  .base-art{left:100px;top:748px;width:290px;height:110px;background:var(--mid-blue);transform:skewX(-10deg);border-radius:4px}

  .reason{display:flex;flex-direction:column;align-items:center;justify-content:center;font-family:"Bebas Neue",sans-serif;color:var(--white)}
  .reason .label{font-size:18px}
  .reason .num{font-size:62px;line-height:.9}
  .reason-1{left:270px;top:321px;width:124px;height:159px;background:var(--navy)}
  .reason-2{left:141px;top:480px;width:129px;height:124px;background:var(--green)}
  .reason-2 .num{color:#f3e46a}
  .reason-3{left:141px;top:604px;width:129px;height:159px;background:var(--yellow)}
  .reason-3 .num{color:var(--orange)}
  .reason-text{font-size:10.6px;line-height:1.38;color:var(--white)}
  .rt-1{left:69px;top:356px;width:198px}
  .rt-2{left:276px;top:526px;width:160px}
  .rt-3{left:274px;top:693px;width:132px}

  .signs-frame{left:518px;top:424px;width:302px;height:456px;border:2px dashed #a9a9a9}
  .signs-tab{left:524px;top:403px;width:192px;height:43px;background:var(--green);font-family:"Bebas Neue",sans-serif;font-size:28px;color:var(--white);padding:6px 0 0 18px}
  .hand-art{left:760px;top:390px;width:84px;height:88px;border-radius:40px 18px 40px 18px;background:var(--yellow)}

  .sign{left:540px;width:270px;display:flex}
  .sign .badge{width:44px;flex:none;text-align:center}
  .sign .tile{width:40px;height:40px;margin:0 auto;display:flex;align-items:center;justify-content:center;font-family:"Bebas Neue",sans-serif;font-size:26px;color:var(--white);border-radius:3px}
  .sign .unit{font-size:10px;font-weight:700;color:#222;margin-top:2px}
  .sign ul{list-style:none;margin-left:16px;font-size:11.4px;line-height:1.35;color:var(--ink);padding-top:2px}
  .s6{top:463px}.s9{top:536px}.s12{top:600px}.s16{top:669px}.s24{top:733px}
  .t-yellow{background:var(--yellow)}.t-green{background:var(--green)}.t-blue{background:var(--mid-blue)}.t-dgreen{background:var(--green-dark)}
  .signs-note{left:537px;top:810px;width:262px;font-size:11.6px;line-height:1.36;font-weight:700;font-style:italic;color:var(--navy)}

  .stats-label{left:120px;top:954px;font-family:"Amatic SC",sans-serif;font-weight:700;font-size:22px;letter-spacing:10px;color:var(--ink)}
  .stat{left:86px;width:400px;display:flex}
  .stat .n{width:37px;flex:none;font-family:"Bebas Neue",sans-serif;font-size:34px;line-height:.9}
  .stat p{font-size:11.6px;line-height:1.38;color:var(--ink)}
  .stat.strong p{font-weight:700}
  .st1{top:986px}.st2{top:1030px}.st3{top:1071px}.st4{top:1127px}
  .n1{color:var(--sky)}.n2{color:var(--pink)}.n3{color:var(--yellow)}.n4{color:var(--green)}
  .hand-chip{left:0;width:60px;height:26px;border-radius:0 14px 14px 0}
  .h1{top:978px;background:var(--sky)}.h2{top:1020px;background:var(--pink)}.h3{top:1064px;background:var(--orange)}.h4{top:1108px;background:var(--yellow)}.h5{top:1150px;background:var(--green)}

  .more-box{left:518px;top:896px;width:303px;height:140px}
  .more-text{left:518px;top:910px;width:303px;text-align:center;font-family:"Bebas Neue",sans-serif;color:var(--white)}
  .more-text .small{font-size:30px;line-height:1}
  .more-text .big{font-size:80px;line-height:.9;color:var(--sky)}
  .about{left:518px;top:1050px;width:303px;text-align:center;font-family:"Bebas Neue",sans-serif;font-size:24px;letter-spacing:16px;color:var(--navy);padding-left:16px}
  .ed{left:518px;top:1076px;width:303px;text-align:center;font-family:"Bebas Neue",sans-serif;font-size:26px;color:var(--yellow)}
  .goto{left:580px;top:1120px;width:180px;display:flex;align-items:center;gap:10px;font-family:"Bebas Neue",sans-serif;font-size:24px;color:var(--navy)}
  .goto span{flex:1;height:2px;background:var(--navy)}
  .url{left:514px;top:1157px;width:310px;display:flex;align-items:center;gap:8px;font-family:"Bebas Neue",sans-serif;font-size:17px;color:var(--navy);white-space:nowrap}
  .url .dot{width:18px;height:18px;border-radius:50%;background:var(--sky);flex:none}
</style>
</head>
<body>
<main class="canvas">
  <header class="abs header"></header>
  <h1 class="abs title-top">EARLY DETECTION</h1>
  <div class="abs title-bottom">AND DIAGNOSIS INFOGRAPHIC</div>
  <div class="abs ribbon">WEEK 1</div>

  <h2 class="abs hand-heading why">WHY IS EARLY DETECTION AND<br>DIAGNOSIS OF AUTISM SO IMPORTANT?</h2>

  <div class="abs head-art" role="img" aria-label="Illustration of a child's head silhouette made of light blue puzzle pieces"></div>
  <div class="abs base-art" role="img" aria-label="Blue shoulders of the child silhouette"></div>

  <div class="abs reason reason-1"><span class="label">REASON</span><span class="num">1</span></div>
  <div class="abs reason reason-2"><span class="label">REASON</span><span class="num">2</span></div>
  <div class="abs reason reason-3"><span class="label">REASON</span><span class="num">3</span></div>

  <p class="abs reason-text rt-1">An early diagnosis can mean a child gains access to important therapies and resources when they can be the most effective. Without the diagnosis, most insurances won’t cover treatments like ABA therapy.</p>
  <p class="abs reason-text rt-2">ABA therapy is shown to be most effective on toddlers and young children because their brains are not completely developed and have an increased potential for developing new learning pathways.</p>
  <p class="abs reason-text rt-3">Children who receive early intervention have improved outcomes and increased success and independence in the long run.</p>

  <h2 class="abs hand-heading how">HOW CAN YOU MAKE SURE<br>A CHILD DOESN'T MISS OUT<br>ON KEY YEARS OF INTERVENTION?</h2>

  <div class="abs signs-frame"></div>
  <div class="abs signs-tab">KNOW THE SIGNS</div>
  <div class="abs hand-art" role="img" aria-label="Illustration of a yellow open hand"></div>

  <div class="abs sign s6"><div class="badge"><div class="tile t-yellow">6</div><div class="unit">MONTHS</div></div>
    <ul><li>• No social smiles or other warm, joyful expressions directed at people</li><li>• Limited or no eye contact</li></ul></div>
  <div class="abs sign s9"><div class="badge"><div class="tile t-green">9</div><div class="unit">MONTHS</div></div>
    <ul><li>• No sharing of vocal sounds, smiles or other nonverbal communication</li></ul></div>
  <div class="abs sign s12"><div class="badge"><div class="tile t-blue">12</div><div class="unit">MONTHS</div></div>
    <ul><li>• No babbling</li><li>• No response to name when called</li><li>• No use of gestures to communicate (e.g. pointing, reaching, waving etc.)</li></ul></div>
  <div class="abs sign s16"><div class="badge"><div class="tile t-dgreen">16</div><div class="unit">MONTHS</div></div>
    <ul><li>• No words</li></ul></div>
  <div class="abs sign s24"><div class="badge"><div class="tile t-yellow">24</div><div class="unit">MONTHS</div></div>
    <ul><li>• No meaningful, two-word phrases</li><li>• Any loss of any previously acquired speech, babbling or social skills</li></ul></div>

  <p class="abs signs-note">You can help increase the success of early detection by having your child evaluated if you see any of these signs.</p>

  <h2 class="abs hand-heading works">WE KNOW THAT EARLY DETECTION<br>AND DIAGNOSIS WORKS...</h2>
  <div class="abs stats-label">STATS</div>

  <div class="abs hand-chip h1" role="img" aria-label="Light blue hand illustration"></div>
  <div class="abs hand-chip h2" role="img" aria-label="Pink hand illustration"></div>
  <div class="abs hand-chip h3" role="img" aria-label="Orange hand illustration"></div>
  <div class="abs hand-chip h4" role="img" aria-label="Yellow hand illustration"></div>
  <div class="abs hand-chip h5" role="img" aria-label="Green hand illustration"></div>

  <div class="abs stat st1"><span class="n n1">1</span><p>Research has shown that a diagnosis of autism at age 2 can be reliable, valid and stable.</p></div>
  <div class="abs stat strong st2"><span class="n n2">2</span><p>Despite all the good that early detection and diagnosis can do, it hasn’t been as successful as it should be…</p></div>
  <div class="abs stat st3"><span class="n n3">3</span><p>In 2016, the QMT conducted a report that showed that only 43 percent of children identified with autism had received comprehensive developmental evaluations by age 3.</p></div>
  <div class="abs stat strong st4"><span class="n n4">4</span><p>According to a QMT study from 2016, even though ASD can be diagnosed as early as age 2 years, most children are not diagnosed with ASD until after age 4 years.</p></div>

  <svg class="abs more-box" viewBox="0 0 303 140" aria-hidden="true"><polygon points="0,0 303,0 303,122 151.5,140 0,122" fill="#1562a4"/></svg>
  <div class="abs more-text"><div class="small">WANT TO LEARN</div><div class="big">MORE</div></div>
  <div class="abs about">ABOUT</div>
  <div class="abs ed">EARLY DETECTION?</div>
  <div class="abs goto"><span></span>GO TO:<span></span></div>
  <div class="abs url"><i class="dot"></i>BRAMBLEWOODKIDSCLINIC.COM/EARLY-DETECTION</div>
</main>
</body>
</html>
```